Upmarket Bathroom and Kitchen ware supplier needs a classy business card design

We are a company based in Fiji, we sell plumbing ware (Kitchen and bathroom taps, Basins,showers, toilets etc) through up market show rooms to individuals and directly through Architects and designers of resorts and holiday houses for new builds and renovations. we are wanting to upgrade our over all look and brand. we are starting with a new logo but will be rebranding the whole business. This project is for a business card design for my management and tales team I would like it to be dark, classy and interesting

Target Market(s)

Resort directors and Management, High end holiday home owners

Contact Information for Business Card

Neil Dawson
Director
+64219473815

Colors

Designer to choose colors to be used in the design.

Requirements
Must have
• Must have an upmarket appearance I like darker charcoal shades but will be guided by the designers
• Please any catch phrases like "Crafting remarkable living rooms" this belongs tpo one of our suppliers so can not be used.
Nice to have
• Double sided, so front dedicated to logo provided and back info about the business and the person.

```html
<!DOCTYPE html>
<html lang="en">
<head>
<meta charset="utf-8">
<title>Lagoon Interiors – Business Card</title>
<link rel="stylesheet" href="https://fonts.googleapis.com/css2?family=Mulish:ital,wght@0,300;0,400;0,500;1,400&family=Parisienne&display=swap">
<style>
  :root {
    --backdrop: #3b3b3c;
    --ink-deep: #022631;
    --ink-glow: #0a333e;
    --paper: #e6e7e9;
    --paper-text: #0f2a33;
    --light-text: #eceeef;
  }
  * { margin: 0; padding: 0; box-sizing: border-box; }
  html, body {
    width: 1200px; height: 815px; overflow: hidden;
    background: var(--backdrop);
  }
  body {
    position: relative;
    font-family: "Mulish", "Helvetica Neue", Arial, sans-serif;
  }
  .card {
    position: absolute;
    left: 349px;
    width: 505px;
    height: 289px;
    box-shadow: 0 14px 28px rgba(0,0,0,0.35);
    overflow: hidden;
  }
  .card-front { top: 88px; background: var(--ink-deep); }
  .card-back  { top: 413px; background: var(--paper); }

  .texture-corner {
    position: absolute;
    width: 90px; height: 110px;
    background: radial-gradient(ellipse at center, var(--ink-glow) 0%, rgba(10,51,62,0) 70%);
  }
  .texture-top-right { right: 0; top: 0; }
  .texture-bottom-left { left: 0; bottom: 0; }

  .front-brand {
    position: absolute;
    left: 0; right: 0; top: 118px;
    text-align: center;
    color: var(--light-text);
    font-weight: 300;
    font-size: 24px;
    letter-spacing: 0.32em;
    text-transform: uppercase;
  }
  .brand-dot {
    display: block;
    width: 34px; height: 34px;
    margin: 0 auto 18px;
    border: 1.5px solid var(--light-text);
    border-radius: 50%;
  }

  .side-band {
    position: absolute;
    top: 32px; width: 17px; height: 225px;
    background: var(--ink-deep);
  }
  .side-band-left { left: 0; }
  .side-band-right { right: 0; }

  .back-brand {
    position: absolute;
    left: 73px; width: 200px; top: 90px;
    text-align: center;
    color: var(--paper-text);
    font-weight: 300;
    font-size: 15px;
    letter-spacing: 0.3em;
    text-transform: uppercase;
  }
  .back-brand .brand-dot {
    width: 26px; height: 26px;
    margin-bottom: 12px;
    border-color: var(--paper-text);
  }

  .contact {
    position: absolute;
    left: 262px; width: 160px; top: 80px;
    text-align: center;
    color: var(--paper-text);
  }
  .contact-name {
    font-size: 15.5px; font-weight: 400; letter-spacing: 0.02em;
    text-transform: uppercase;
  }
  .contact-role {
    margin-top: 6px;
    font-size: 11px; font-style: italic; color: #2c4a54;
  }
  .contact-phone {
    margin-top: 15px;
    font-size: 11.5px; font-weight: 500; letter-spacing: 0.05em;
  }
  .tagline {
    position: absolute;
    left: 0; right: 0; top: 204px;
    text-align: center;
    font-family: "Parisienne", "Brush Script MT", cursive;
    font-size: 16px;
    color: #2a4a55;
    letter-spacing: 0.03em;
  }
</style>
</head>
<body>
  <section class="card card-front" aria-label="Card front">
    <div class="texture-corner texture-top-right" role="img" aria-label="Faint geometric pattern"></div>
    <div class="texture-corner texture-bottom-left" role="img" aria-label="Faint geometric pattern"></div>
    <div class="front-brand"><span class="brand-dot"></span>Lagoon Interiors</div>
  </section>

  <section class="card card-back" aria-label="Card back">
    <div class="side-band side-band-left"></div>
    <div class="side-band side-band-right"></div>
    <div class="back-brand"><span class="brand-dot"></span>Lagoon Interiors</div>
    <div class="contact">
      <p class="contact-name">Neil Dawson</p>
      <p class="contact-role">Director</p>
      <p class="contact-phone">(+64) 219 473 815</p>
    </div>
    <p class="tagline">“because everyone deserves a little taste of the lagoon”</p>
  </section>
</body>
</html>
```